Need a professional card design. Tallowmere building company specialise in residential and commercial builds. New homes, additions & renovations.
Wanting a card with creativity and professionalism.
Want card that utilises logo.

Back and front.

I have just created a logo, and want to use it on the business card.
Attached a copy of the logo.
Attached is also a current business card which I wish to redesign

please utilise both sides

Residential

• Reg# 58306

```html
<!DOCTYPE html>
<html lang="en">
<head>
<meta charset="utf-8">
<title>Tallowmere Building Co — Business Card</title>
<link href="https://fonts.googleapis.com/css2?family=Open+Sans:wght@400;600;700&display=swap" rel="stylesheet">
<style>
  :root {
    --orange: #f2a73b;
    --orange-deep: #e8962a;
    --orange-line: #f6bd63;
    --ink: #262626;
    --white: #ffffff;
    --stage: #3b3b3d;
  }
  * { box-sizing: border-box; margin: 0; padding: 0; }
  html, body { width: 1200px; height: 900px; overflow: hidden; }
  body {
    background: var(--stage);
    font-family: "Open Sans", Arial, sans-serif;
    color: var(--ink);
    position: relative;
  }
  .card {
    position: absolute;
    left: 280px;
    width: 640px;
    height: 391px;
    border-radius: 26px;
    overflow: hidden;
  }
  .card--back { top: 30px; background: var(--orange); }
  .card--front { top: 479px; background: var(--white); }

  .card__wave { position: absolute; inset: 0; }

  /* Wordmark standing where the logo sits */
  .wordmark {
    position: absolute;
    display: flex;
    align-items: center;
    gap: 12px;
    font-weight: 700;
    color: var(--ink);
    line-height: 1.05;
  }
  .wordmark__dot {
    width: 18px; height: 18px;
    border-radius: 50%;
    background: var(--ink);
    flex: none;
  }
  .card--front .wordmark { left: 50px; top: 96px; font-size: 30px; }
  .card--back .wordmark {
    left: 0; right: 0;
    top: 112px;
    justify-content: center;
    font-size: 36px;
  }

  .tagline {
    position: absolute;
    left: 0; right: 0;
    top: 190px;
    text-align: center;
    color: var(--white);
    font-size: 19px;
    line-height: 1.5;
  }

  .reg {
    position: absolute;
    right: 40px; top: 30px;
    font-size: 11px;
  }
  .person {
    position: absolute;
    right: 40px; top: 66px;
    text-align: right;
  }
  .person__name { color: var(--orange-deep); font-size: 22px; font-weight: 600; }
  .person__role { font-size: 15px; font-weight: 600; }

  .contacts {
    position: absolute;
    right: 40px; top: 160px;
    list-style: none;
    font-size: 16px;
    line-height: 26px;
  }
  .contacts li { display: flex; justify-content: flex-end; align-items: center; gap: 8px; }
  .contacts li + li { margin-top: 0; }
  .contacts svg { width: 15px; height: 15px; fill: var(--ink); flex: none; }
  .contacts__email { margin-top: 18px !important; }
</style>
</head>
<body>

<section class="card card--back" aria-label="Card back">
  <div class="wordmark"><span class="wordmark__dot"></span>Tallowmere Building Co</div>
  <p class="tagline">New Homes, Additions &amp; Renovations<br>Residential &amp; Commercial Builders</p>
</section>

<section class="card card--front" aria-label="Card front">
  <svg class="card__wave" viewBox="0 0 640 391" preserveAspectRatio="none" aria-hidden="true">
    <path d="M0,232 C210,236 400,176 640,128" fill="none" stroke="var(--orange)" stroke-width="3"/>
    <path d="M0,248 C210,252 400,192 640,144 L640,391 L0,391 Z" fill="var(--orange)"/>
    <path d="M0,258 C210,262 400,202 640,154" fill="none" stroke="var(--orange-line)" stroke-width="2"/>
  </svg>

  <div class="wordmark"><span class="wordmark__dot"></span>Tallowmere<br>Building Co</div>

  <p class="reg">Reg# 58306</p>

  <div class="person">
    <p class="person__name">Corin Halvey</p>
    <p class="person__role">director</p>
  </div>

  <ul class="contacts">
    <li>08 9417 2650
      <svg viewBox="0 0 16 16" aria-label="phone"><path d="M3.5 1l3 3-1.8 1.8a9 9 0 0 0 5.5 5.5L12 9.5l3 3-2 2C6.5 14 2 9.5 1.5 3z"/></svg>
    </li>
    <li>08 9417 2650
      <svg viewBox="0 0 16 16" aria-label="fax"><rect x="4" y="1" width="8" height="5"/><rect x="1" y="6" width="14" height="7" rx="1"/><rect x="4" y="11" width="8" height="4" fill="#fff" stroke="#262626"/></svg>
    </li>
    <li>0412 508 193
      <svg viewBox="0 0 16 16" aria-label="mobile"><path d="M4 1h8v14H4z M5.5 2.5v9h5v-9z" fill-rule="evenodd"/></svg>
    </li>
    <li class="contacts__email">tallowmerebuildingco@mailbox.com
      <svg viewBox="0 0 16 16" aria-label="email"><path d="M1 3h14v10H1z"/><path d="M1.5 3.5L8 9l6.5-5.5" fill="none" stroke="#f2a73b" stroke-width="1.2"/></svg>
    </li>
  </ul>

  <address class="address" style="position:absolute;left:50px;top:300px;font-size:17px;line-height:24px;font-style:normal;">42 Brackenridge Way<br>Ellerton<br>WA 6031</address>
</section>

</body>
</html>
```